RESIDENTIAL CONSTRUCTION

We are a company that specializes in building custom residential homes, the design should also emphasize that quality and service is our priority.

Industry/Entity Type

Construction Company

Contact Information for Business Card

Contact Person: Tobias Lindqvar
Company Address: 463 Westbrook Ave San Jose , Ca 95112
Phone Number : 408-731-2946
Email Address: Oakfieldcrafters731@mailvessel.net

Font styles to use
Sans Serif

Colors
ec1f27

Requirements
Must have
• CSLB # 7362519
Nice to have
• needs to have same color as logo i uploaded, we will be printing these on a clear plastic card.

```html
<!DOCTYPE html>
<html lang="en">
<head>
<meta charset="utf-8">
<title>Oakfield Crafters – Business Card</title>
<link href="https://fonts.googleapis.com/css2?family=Bebas+Neue&family=Lato:wght@400&display=swap" rel="stylesheet">
<style>
  :root {
    --backdrop: #5b5b5b;
    --card-red: #bf1e2e;
    --ink-black: #000000;
    --ink-soft: #161616;
    --paper-white: #ffffff;
    --text-light: #ffffff;
  }
  * { margin: 0; padding: 0; box-sizing: border-box; }
  html, body {
    width: 1200px;
    height: 802px;
    overflow: hidden;
    background: var(--backdrop);
  }
  .canvas {
    position: relative;
    width: 1200px;
    height: 802px;
  }
  .card {
    position: absolute;
    top: 274px;
    width: 443px;
    height: 265px;
    overflow: hidden;
    box-shadow: 0 3px 6px rgba(0,0,0,0.45);
  }
  .card--front {
    left: 136px;
    background: var(--card-red);
  }
  .card--back {
    left: 624px;
    background: var(--paper-white);
    display: flex;
    align-items: center;
    justify-content: center;
  }
  .front-artwork {
    position: absolute;
    left: 0;
    top: 0;
    width: 215px;
    height: 265px;
    background: linear-gradient(160deg, var(--ink-soft) 0%, var(--ink-black) 55%);
    clip-path: polygon(0 0, 135px 0, 213px 265px, 0 265px);
  }
  .contact {
    position: absolute;
    right: 21px;
    top: 0;
    text-align: right;
    color: var(--text-light);
    font-family: 'Lato', sans-serif;
    font-size: 12.5px;
    line-height: 16px;
  }
  .contact__name {
    position: absolute;
    right: 0;
    top: 60px;
    white-space: nowrap;
    font-family: 'Bebas Neue', sans-serif;
    font-weight: 400;
    font-size: 22px;
    line-height: 22px;
    letter-spacing: 0.2px;
  }
  .contact__line {
    position: absolute;
    right: 0;
    white-space: nowrap;
  }
  .contact__license { top: 102px; }
  .contact__address { top: 138px; }
  .contact__phone { top: 186px; }
  .contact__email { top: 202px; }
  .contact__icon {
    display: inline-block;
    width: 12px;
    height: 10px;
    margin-left: 2px;
    vertical-align: -1px;
    fill: var(--text-light);
  }
  .brand {
    display: flex;
    align-items: center;
    gap: 6px;
  }
  .brand__square {
    width: 14px;
    height: 14px;
    background: var(--card-red);
  }
  .brand__name {
    font-family: 'Bebas Neue', sans-serif;
    font-weight: 400;
    font-size: 40px;
    line-height: 1;
    color: var(--card-red);
    white-space: nowrap;
  }
</style>
</head>
<body>
<main class="canvas">
  <section class="card card--front">
    <div class="front-artwork" role="img" aria-label="Black and white illustration of a house roof with a pencil and a hand saw"></div>
    <div class="contact">
      <h1 class="contact__name">TOBIAS LINDQVAR</h1>
      <p class="contact__line contact__license">CSLB # 7362519</p>
      <p class="contact__line contact__address">463 Westbrook Ave San Jose<br>Ca 95112</p>
      <p class="contact__line contact__phone">408-731-2946<svg class="contact__icon" viewBox="0 0 12 10" aria-hidden="true"><path d="M1 3.5 C1 1.5 11 1.5 11 3.5 L11 4.5 L8.5 4.5 L8.5 3.3 L3.5 3.3 L3.5 4.5 L1 4.5 Z M3 5 L9 5 L10.5 9.5 L1.5 9.5 Z"/></svg></p>
      <p class="contact__line contact__email">Oakfieldcrafters731@mailvessel.net<svg class="contact__icon" viewBox="0 0 12 10" aria-hidden="true"><path d="M0.5 1 L11.5 1 L11.5 9 L0.5 9 Z M1.5 2 L6 5.6 L10.5 2 Z" fill-rule="evenodd"/></svg></p>
    </div>
  </section>
  <section class="card card--back">
    <div class="brand">
      <span class="brand__square" aria-hidden="true"></span>
      <span class="brand__name">OAKFIELD CRAFTERS</span>
    </div>
  </section>
</main>
</body>
</html>
```